Exciting letterhead design for startup company

We need a A4 letterhead designing.

See attached file which contains the logo (on 3 different coloured backgrounds) and then the address and contact information. It also contains 4 colours that can be used.

Looking for an imaginative design. We are a young, fresh startup website design company so need a letterhead that reflects our industry.

Font styles to use
Sans Serif

```html
<!DOCTYPE html>
<html lang="en">
<head>
<meta charset="utf-8">
<title>PixelCart Letterhead</title>
<link rel="stylesheet" href="https://fonts.googleapis.com/css2?family=Arimo:wght@400;700&display=swap">
<style>
  :root {
    --header-dark: #1c1c20;
    --accent-blue: #3ea4dc;
    --footer-gold: #f2b328;
    --paper: #ffffff;
    --ink-light: #ffffff;
    --ink-dark: #1c1c20;
  }
  * { margin: 0; padding: 0; box-sizing: border-box; }
  html, body { width: 849px; height: 1200px; overflow: hidden; background: var(--paper); }
  body { font-family: "Arimo", Arial, sans-serif; }
  .letterhead { position: relative; width: 849px; height: 1200px; background: var(--paper); }
  .letterhead-header {
    position: absolute; top: 0; left: 0; width: 100%; height: 128px;
    background: var(--header-dark);
  }
  .brand-name {
    position: absolute; left: 56px; top: 36px;
    font-size: 50px; font-weight: 700; letter-spacing: -1px;
    color: var(--ink-light); line-height: 1;
  }
  .contact-list {
    position: absolute; left: 520px; top: 36px; list-style: none;
    color: var(--ink-light); font-size: 15px; line-height: 19px;
  }
  .contact-item { display: flex; align-items: flex-start; margin-bottom: 8px; }
  .contact-item:nth-child(3) { margin-top: -1px; }
  .contact-icon { width: 16px; height: 16px; margin-right: 14px; margin-top: 2px; flex-shrink: 0; }
  .letterhead-footer {
    position: absolute; left: 0; bottom: 0; width: 100%; height: 42px;
    background: var(--footer-gold);
    display: flex; align-items: center; justify-content: center;
    color: var(--ink-dark); font-size: 15px;
  }
</style>
</head>
<body>
  <div class="letterhead">
    <header class="letterhead-header">
      <div class="brand-name">PixelCart</div>
      <ul class="contact-list">
        <li class="contact-item">
          <svg class="contact-icon" viewBox="0 0 16 16" aria-hidden="true">
            <path d="M2 6c0-2 3-3 6-3s6 1 6 3v1h-3V5.5H5V7H2z M4 8h8l1 5H3z" fill="var(--accent-blue)"/>
          </svg>
          <span>0845 555 0198</span>
        </li>
        <li class="contact-item">
          <svg class="contact-icon" viewBox="0 0 16 16" aria-hidden="true">
            <rect x="1" y="3.5" width="14" height="9" rx="1" fill="var(--accent-blue)"/>
            <path d="M1.5 4l6.5 5 6.5-5" fill="none" stroke="var(--header-dark)" stroke-width="1.2"/>
          </svg>
          <span>hello@pixelcart.co.uk</span>
        </li>
        <li class="contact-item">
          <svg class="contact-icon" viewBox="0 0 16 16" aria-hidden="true">
            <path d="M8 1a5 5 0 0 1 5 5c0 4-5 9-5 9S3 10 3 6a5 5 0 0 1 5-5z" fill="var(--accent-blue)"/>
            <circle cx="8" cy="6" r="2" fill="var(--header-dark)"/>
          </svg>
          <span>PixelCart Limited, Suite 4,<br>Harbour Court, Bristol BS1 4QA</span>
        </li>
      </ul>
    </header>
    <footer class="letterhead-footer">Registered in England &amp; Wales. Company No 01234567.</footer>
  </div>
</body>
</html>
```